Update our OBGYN business card look and info

We are an OBGYN office. Our logo is nice but would like to "woman" part of the logo to be a darker color, to contrast with the flower that surrounds it. Maybe make our practice name Harbor Bloom Care Clinic more feminine. Our practice caters to women only. All providers and staff are female.

Target Market(s)

Females 16-65.

Industry/Entity Type

Business

Contact Information for Business Card

See attached upload. The ONLY CHANGE to the information is DELETE the name Dorothy Kemplin, Midwife and REPLACE with Greta Poundsworth, Midwife

Logo Text

Harbor Bloom Care Clinic Obstetrics & Gynecology

Font styles to use
Serif
Script

Colors
85cae6
0692cd
33a6d7
85abd2
f59195
eea4c8
cadf82
fac994
d3a5cc

```html
<!DOCTYPE html>
<html lang="en">
<head>
<meta charset="utf-8">
<title>Harbor Bloom Care Clinic – Business Card</title>
<link rel="stylesheet" href="https://fonts.googleapis.com/css2?family=EB+Garamond:wght@400;500&display=swap">
<style>
  :root {
    --bg: #e9edf0;
    --card: #ffffff;
    --blue-deep: #0692cd;
    --blue-mid: #33a6d7;
    --blue-light: #85cae6;
    --text-blue: #1e8fc8;
    --white: #ffffff;
  }
  * { margin: 0; padding: 0; box-sizing: border-box; }
  html, body { width: 1200px; height: 880px; overflow: hidden; }
  body {
    background: var(--bg);
    font-family: "EB Garamond", Georgia, serif;
    display: flex;
    flex-direction: column;
    align-items: center;
    justify-content: center;
    gap: 40px;
  }
  .card {
    position: relative;
    width: 660px;
    height: 377px;
    background: var(--card);
    border-radius: 22px;
    overflow: hidden;
    box-shadow: 0 6px 18px rgba(0,0,0,0.12);
  }
  /* Back */
  .card-back .brand {
    position: absolute;
    top: 130px; left: 0; right: 0;
    display: flex; align-items: center; justify-content: center; gap: 14px;
  }
  .brand-dot {
    width: 40px; height: 40px; border-radius: 50%;
    background: var(--blue-mid);
  }
  .brand-name {
    font-size: 30px; font-weight: 500; color: var(--text-blue);
    letter-spacing: 0.5px;
  }
  .card-back .website {
    position: absolute; top: 228px; left: 0; right: 0;
    text-align: center; font-size: 17px; letter-spacing: 2px; color: var(--text-blue);
  }
  /* Front */
  .waves { position: absolute; inset: 0; }
  .card-front .brand {
    position: absolute; top: 78px; left: 40px;
    display: flex; align-items: center; gap: 12px;
  }
  .card-front .brand-dot { width: 34px; height: 34px; }
  .card-front .brand-name { font-size: 27px; }
  .specialty {
    position: absolute; top: 128px; left: 40px;
    font-size: 17px; font-weight: 500; letter-spacing: 1.5px; color: var(--text-blue);
  }
  .providers {
    position: absolute; top: 22px; right: 34px;
    list-style: none; text-align: right;
    font-size: 15px; line-height: 1.22; color: var(--text-blue);
  }
  .contact {
    position: absolute; right: 30px; top: 196px;
    text-align: right; color: var(--white); font-size: 15px; line-height: 1.3;
  }
  .contact .address { margin-bottom: 10px; }
  .contact-line { display: flex; justify-content: flex-end; align-items: center; gap: 8px; }
  .icon { width: 15px; height: 15px; flex: none; }
</style>
</head>
<body>

<section class="card card-back">
  <div class="brand">
    <span class="brand-dot"></span>
    <span class="brand-name">Harbor Bloom Care Clinic</span>
  </div>
  <p class="website">www.harborbloomcare.com</p>
</section>

<section class="card card-front">
  <svg class="waves" viewBox="0 0 660 377" aria-hidden="true">
    <path d="M0,300 C170,298 268,268 300,178 C296,270 200,320 0,332 Z" fill="var(--blue-light)"/>
    <path d="M0,377 L0,346 C170,334 272,318 330,232 C380,156 470,140 660,130 L660,377 Z" fill="var(--blue-deep)"/>
    <path d="M150,377 C270,346 330,292 372,224 C420,160 520,150 640,142" fill="none" stroke="var(--white)" stroke-width="6"/>
  </svg>

  <div class="brand">
    <span class="brand-dot"></span>
    <span class="brand-name">Harbor Bloom Care Clinic</span>
  </div>
  <p class="specialty">OBSTETRICS &amp; GYNECOLOGY</p>

  <ul class="providers">
    <li>Renata Fulbright, MD</li>
    <li>Lydia Vantreese, MD</li>
    <li>Nadine Crowell, MD</li>
    <li>Greta Poundsworth, Midwife</li>
    <li>Priya Halvorsen, Midwife</li>
  </ul>

  <div class="contact">
    <p class="address">418 Larkspur Ave, Ste 3B<br>Fairmont, GA 31990-4417</p>
    <p class="contact-line">555-201-4738
      <svg class="icon" viewBox="0 0 16 16"><rect x="4" y="1" width="8" height="14" rx="2" fill="none" stroke="#fff" stroke-width="1.6"/><circle cx="8" cy="12.3" r="0.9" fill="#fff"/></svg>
    </p>
    <p class="contact-line">555-201-4153
      <svg class="icon" viewBox="0 0 16 16"><rect x="2" y="6" width="12" height="7" rx="1.5" fill="none" stroke="#fff" stroke-width="1.6"/><rect x="4.5" y="2" width="7" height="4" fill="none" stroke="#fff" stroke-width="1.4"/></svg>
    </p>
    <p class="contact-line">www.harborbloomcare.com
      <svg class="icon" viewBox="0 0 16 16"><circle cx="8" cy="8" r="6.2" fill="none" stroke="#fff" stroke-width="1.4"/><ellipse cx="8" cy="8" rx="2.6" ry="6.2" fill="none" stroke="#fff" stroke-width="1.2"/><line x1="1.8" y1="8" x2="14.2" y2="8" stroke="#fff" stroke-width="1.2"/></svg>
    </p>
  </div>
</section>

</body>
</html>
```